Fire Risk Assessment App needs a sleek UI design

I need a sleek, modern but professional design for my 5 page Fire Risk Assessment App. Include gradient background, fire themed colours including reds, yellows, light orange and a touch of black. Design must ooze simplicity and professionalism. This is for the UK market. See attached images and word doc for more information.

Target Market(s)

General public and business owners

Industry/Entity Type

Technology / Fire Safety

Colors
00AB8E
00BBA5
67D7C9
C6EFE9
E9F9F6
59FF00
82FF00
B8FF75
E3FFCB
F4FFEA
FFC000
F8CF3A
FAE287
FDF2CF
FEFAEE
F0912C
F2A743
F7CA91
FBE8D2
FDF5EE
EE7325
F08F49
F5BC92
FAE3D3
FDF4ED
EB3D1F
EC4F4E
F09395
F8D3D4
FCEDEE

```html
<!DOCTYPE html>
<html lang="en">
<head>
<meta charset="utf-8">
<title>Fire Risk Assessment – Question</title>
<link href="https://fonts.googleapis.com/css2?family=Outfit:wght@300;400;500&display=swap" rel="stylesheet">
<style>
:root{
  --bg:#121212;
  --bg-warm:#4a1a16;
  --card:#1f1f1f;
  --field:#1c1c1c;
  --btn-dark:#1e1e1e;
  --text:#ffffff;
  --muted:#8a8a8a;
  --soft:#e6e6e6;
  --teal:#1fc9a8;
  --track:#333333;
  --grey-btn:#7d7d7d;
  --line:#3a3a3a;
  --pink:#f0145a;
  --orange:#ff6a10;
}
*{box-sizing:border-box;margin:0;padding:0}
html,body{width:1200px;height:2597px;overflow:hidden}
body{
  font-family:"Outfit",sans-serif;color:var(--text);
  background:radial-gradient(ellipse 900px 700px at 0 0,var(--bg-warm),rgba(18,18,18,0) 100%),var(--bg);
  position:relative;
}
.abs{position:absolute}
.back-btn{left:50px;top:185px;width:159px;height:159px;border-radius:36px;background:var(--btn-dark);display:flex;align-items:center;justify-content:center}
.save-btn{left:806px;top:185px;width:345px;height:159px;border-radius:36px;background:var(--btn-dark);display:flex;align-items:center;justify-content:center;font-size:43px}
.flame{left:62px;top:418px}
.title{left:198px;top:405px;font-size:66px;font-weight:400}
.subtitle{left:200px;top:486px;font-size:35px;color:var(--muted);font-weight:300}
.progress{left:50px;top:575px;width:1101px;height:3px;background:var(--track)}
.progress i{position:absolute;left:0;top:-6px;width:387px;height:15px;border-radius:8px;background:var(--teal)}
.section-score{left:50px;top:665px;font-size:56px;color:var(--muted);font-weight:300}
.section-score small{font-size:36px}
.drop-btn{left:557px;top:660px;width:80px;height:80px;border-radius:16px;background:#252525;display:flex;align-items:center;justify-content:center}
.bolt{left:1040px;top:628px}
.topic{left:50px;top:780px;font-size:54px}
.clause{left:50px;top:870px;font-size:36px;color:var(--soft);font-weight:300}
.card{left:50px;top:982px;width:1101px;height:1256px;border-radius:50px;background:var(--card)}
.q-num{left:98px;top:1055px;font-size:56px;color:var(--muted);font-weight:300}
.q-num small{font-size:36px}
.prev-q{left:692px;top:1050px;width:77px;height:77px;border-radius:50%;background:var(--grey-btn);display:flex;align-items:center;justify-content:center}
.next-q{left:794px;top:1050px;width:307px;height:77px;border-radius:39px;background:var(--grey-btn);display:flex;align-items:center;justify-content:center;font-size:36px}
.q-progress{left:98px;top:1176px;width:1003px;height:3px;background:var(--track)}
.q-progress i{position:absolute;left:0;top:-6px;width:730px;height:15px;border-radius:8px;background:var(--teal)}
.question{left:98px;top:1225px;width:1000px;font-size:48px;line-height:83px;color:var(--soft)}
.option{top:1470px;display:flex;align-items:center;gap:36px;font-size:43px}
.radio{width:62px;height:62px;border-radius:50%;border:5px solid #6a6a6a}
.radio.on{border:none;background:#fff;display:flex;align-items:center;justify-content:center}
.radio.on::after{content:"";width:24px;height:24px;border-radius:50%;background:#111}
.note{left:98px;top:1620px;width:1003px;height:158px;border-radius:60px;border:3px solid var(--line);background:var(--field);display:flex;align-items:center;justify-content:space-between;padding:0 48px 0 42px;font-size:48px}
.upload{left:98px;top:1818px;width:1003px;height:370px;border-radius:50px;border:3px solid var(--line);background:var(--field);display:flex;align-items:center;justify-content:center;gap:34px;font-size:43px}
.footer-line{left:0;top:2293px;width:1200px;height:2px;background:#2a2a2a}
.foot-label{left:50px;top:2360px;font-size:35px;color:var(--muted)}
.foot-score{left:50px;top:2418px;font-size:64px}
.foot-score small{font-size:36px;color:var(--muted)}
.next-section{left:733px;top:2344px;width:418px;height:159px;border-radius:50px;background:linear-gradient(135deg,var(--pink),var(--orange));display:flex;align-items:center;justify-content:center;gap:40px;font-size:44px}
</style>
</head>
<body>
<div class="abs back-btn"><svg width="34" height="48" viewBox="0 0 34 48"><path d="M26 4 8 24l18 20" fill="none" stroke="#fff" stroke-width="5" stroke-linecap="round" stroke-linejoin="round"/></svg></div>
<div class="abs save-btn">Save &amp; Close</div>

<svg class="abs flame" width="84" height="104" viewBox="0 0 84 104"><path d="M42 6c4 18 34 32 34 60a34 34 0 0 1-68 0c0-14 8-24 14-30 0 10 4 18 10 20-6-20 4-38 10-50z" fill="none" stroke="#e8e8e8" stroke-width="8" stroke-linejoin="round"/><path d="M30 74a12 12 0 0 0 24 0" fill="none" stroke="#e8e8e8" stroke-width="7" stroke-linecap="round"/></svg>
<div class="abs title">Fire Risk Assessment</div>
<div class="abs subtitle">Fire Hazards</div>
<div class="abs progress"><i></i></div>

<div class="abs section-score">Section : 7.00 <small>/ 30.00</small></div>
<div class="abs drop-btn"><svg width="32" height="20" viewBox="0 0 32 20"><path d="M4 4l12 12L28 4" fill="none" stroke="#fff" stroke-width="4" stroke-linecap="round" stroke-linejoin="round"/></svg></div>
<svg class="abs bolt" width="112" height="146" viewBox="0 0 112 146"><circle cx="56" cy="70" r="55" fill="#262626"/><circle cx="56" cy="70" r="40" fill="#333"/><path d="M74 4 32 78h34l-28 66 48-86H54z" fill="none" stroke="#f04a2a" stroke-width="5" stroke-linejoin="round"/></svg>

<div class="abs topic">Electronic sources of ignition</div>
<div class="abs clause">Clause 13 &amp; Annex B</div>

<div class="abs card"></div>
<div class="abs q-num">Q : 7 <small>/ 10</small></div>
<div class="abs prev-q"><svg width="20" height="30" viewBox="0 0 20 30"><path d="M15 4 5 15l10 11" fill="none" stroke="#fff" stroke-width="4" stroke-linecap="round" stroke-linejoin="round"/></svg></div>
<div class="abs next-q">Next Question</div>
<div class="abs q-progress"><i></i></div>
<div class="abs question">Are reasonable measures taken to prevent fires of electrical origin?</div>

<div class="abs option" style="left:98px"><span class="radio on"></span>Yes</div>
<div class="abs option" style="left:476px"><span class="radio"></span>No</div>
<div class="abs option" style="left:855px"><span class="radio"></span>N/A</div>

<div class="abs note"><span>No, Electric sockets are overloaded</span>
<svg width="50" height="68" viewBox="0 0 50 68"><rect x="15" y="3" width="20" height="40" rx="10" fill="none" stroke="#fff" stroke-width="4"/><path d="M5 30a20 20 0 0 0 40 0M25 50v14" fill="none" stroke="#fff" stroke-width="4" stroke-linecap="round"/></svg></div>

<div class="abs upload"><svg width="68" height="56" viewBox="0 0 68 56"><path d="M6 14h14l6-10h16l6 10h14v38H6z" fill="none" stroke="#fff" stroke-width="4" stroke-linejoin="round"/><circle cx="34" cy="31" r="10" fill="none" stroke="#fff" stroke-width="4"/></svg><span>Upload Photo</span></div>

<div class="abs footer-line"></div>
<div class="abs foot-label">Section</div>
<div class="abs foot-score">7.00 <small>/ 30.00</small></div>
<div class="abs next-section"><span>Next Section</span><svg width="26" height="44" viewBox="0 0 26 44"><path d="M4 4l18 18L4 40" fill="none" stroke="#fff" stroke-width="4" stroke-linecap="round" stroke-linejoin="round"/></svg></div>
</body>
</html>
```